Corporate Capability Statement for Brenwick Procurement Partners LLC

Create Corporate Capability Statement for Consulting Firm small business start-up. Minority woman-owned consulting firm based in Washington, DC metropolitan area with a target market of the local and federal government. Would like see some area government images such as buildings or monuments. Sending previous Cape Statement which really need a complete over haul. Looking for something eye-catching and creates a strong presence. The final design should communicate our numerous service offerings.

Target Market(s)

Government

Industry/Entity Type

Management Consulting

Font styles to use
Serif
Sans Serif

Requirements
Must have
• Must be able to showcase all service offerings on one-page. Usage of company colors blue and gray.
Nice to have
• images of Washington DC or government monuments illustrated in the document.
• Nice to have my contact info listed on the cape statement somewhere with the updated info below:
• Company POC: Marisa T. Holloway, CEO & Founder
• Oakmere, MD 20999 | 202.555.0147 | info@brenwickpartners-example.com | www.brenwickpartners-example.com

```html
<!DOCTYPE html>
<html lang="en">
<head>
<meta charset="utf-8">
<title>Capabilities Statement – Brenwick Procurement Partners</title>
<link href="https://fonts.googleapis.com/css2?family=Open+Sans:wght@400;600;700;800&family=PT+Sans+Narrow:wght@400;700&display=swap" rel="stylesheet">
<style>
  :root {
    --navy: #1e3570;
    --blue: #2f6fc7;
    --arrow-blue: #3b6fd2;
    --accent-blue: #3f86d6;
    --footer: #3a4fa6;
    --footer-label: #7fb1f0;
    --gray-band: #e6e7ea;
    --gray-col: #e9eaec;
    --text: #2a2a2e;
    --white: #ffffff;
    --top-strip: #8fb1e4;
  }
  * { box-sizing: border-box; margin: 0; padding: 0; }
  html, body { width: 895px; height: 1200px; overflow: hidden; background: #f4f4f4; }
  .sheet {
    position: relative; width: 895px; height: 1200px; background: var(--white);
    font-family: "Open Sans", Arial, sans-serif; color: var(--text); overflow: hidden;
  }
  .top-strip { position: absolute; left: 0; top: 0; width: 895px; height: 11px; background: var(--top-strip); }
  .hero { position: absolute; left: 0; top: 11px; width: 895px; height: 250px; }
  .brand { position: absolute; left: 14px; top: 150px; display: flex; align-items: center; gap: 10px; }
  .brand-mark { width: 26px; height: 26px; background: var(--navy); }
  .brand-name { font-weight: 700; color: var(--navy); font-size: 22px; line-height: 1.05; letter-spacing: 0.5px; }
  .brand-name span { display: block; font-size: 11.5px; letter-spacing: 1.6px; }
  .title { position: absolute; right: 24px; top: 22px; text-align: right; font-weight: 800; font-size: 32px; line-height: 1.12; letter-spacing: 0.3px; }
  .title .line-a { color: var(--navy); padding-right: 80px; display: block; }
  .title .line-b { color: var(--white); display: block; }
  .section-head { position: absolute; font-family: "PT Sans Narrow", "Arial Narrow", sans-serif; font-weight: 700; font-size: 31px; color: var(--navy); letter-spacing: -0.2px; line-height: 1.2; }
  .section-head em { font-style: normal; color: var(--blue); }
  .head-overview { left: 62px; top: 232px; }
  .head-services { right: 10px; top: 235px; }
  .head-why { left: 82px; top: 712px; color: var(--blue); }
  .overview-band { position: absolute; left: 0; top: 230px; width: 460px; height: 44px; background: var(--gray-band); }
  .why-band { position: absolute; left: 0; top: 705px; width: 460px; height: 46px; }
  .overview-text {
    position: absolute; left: 11px; top: 284px; width: 438px;
    font-size: 16.4px; line-height: 27.4px; text-align: justify; hyphens: auto;
  }
  .why-text {
    position: absolute; left: 11px; top: 762px; width: 438px;
    font-family: "PT Sans Narrow", "Arial Narrow", sans-serif;
    font-size: 19px; line-height: 23px; text-align: justify; hyphens: auto;
  }
  .why-text p + p { margin-top: 22px; }
  .services-col { position: absolute; left: 460px; top: 270px; width: 122px; height: 844px; background: var(--gray-col); }
  .service { position: absolute; left: 460px; width: 435px; border-bottom: 2px solid var(--gray-band); }
  .service-label { position: absolute; left: 0; width: 122px; text-align: center; font-family: "PT Sans Narrow", "Arial Narrow", sans-serif; font-weight: 700; font-size: 16px; line-height: 19px; color: var(--blue); }
  .service-icon { position: absolute; left: 16px; width: 96px; height: 50px; }
  .service-text { position: absolute; left: 128px; width: 300px; font-size: 13px; line-height: 17.4px; text-align: justify; hyphens: auto; }
  .footer { position: absolute; left: 0; top: 1114px; width: 895px; height: 86px; background: var(--footer); color: var(--white); font-family: "PT Sans Narrow", "Arial Narrow", sans-serif; }
  .footer-title { position: absolute; left: 15px; top: 25px; font-weight: 700; font-size: 27px; }
  .contact { position: absolute; font-size: 19px; white-space: nowrap; }
  .contact .label { color: var(--footer-label); display: inline-block; }
  .c-poc { left: 230px; top: 12px; } .c-poc .label { width: 128px; }
  .c-phone { left: 230px; top: 46px; } .c-phone .label { width: 118px; }
  .c-email { left: 507px; top: 12px; } .c-email .label { width: 74px; }
  .c-addr { left: 507px; top: 46px; } .c-addr .label { width: 74px; }
</style>
</head>
<body>
<div class="sheet">
  <div class="top-strip"></div>

  <svg class="hero" viewBox="0 0 895 250" width="895" height="250">
    <defs>
      <linearGradient id="photo-tones" x1="0" y1="0" x2="0" y2="1">
        <stop offset="0" stop-color="#1f5fb4"/>
        <stop offset="0.45" stop-color="#6f9fd6"/>
        <stop offset="0.7" stop-color="#eef0f2"/>
        <stop offset="1" stop-color="#3f6a35"/>
      </linearGradient>
    </defs>
    <polygon role="img" aria-label="Photograph of a white government building with columns and a flag under a blue sky" points="432,0 895,0 895,222 222,249 222,232" fill="url(#photo-tones)"/>
    <polygon points="780,185 895,165 895,222 700,222" fill="var(--accent-blue)"/>
    <polygon points="240,200 380,215 430,249 180,249" fill="var(--accent-blue)"/>
  </svg>

  <div class="brand">
    <div class="brand-mark"></div>
    <div class="brand-name">BRENWICK<span>PROCUREMENT PARTNERS</span></div>
  </div>

  <div class="title"><span class="line-a">CAPABILITIES</span><span class="line-b">STATEMENT</span></div>

  <div class="overview-band"></div>
  <h2 class="section-head head-overview">COMPANY <em>OVERVIEW</em></h2>
  <h2 class="section-head head-services">BUSINESS <em>SERVICE</em> OFFERINGS</h2>

  <p class="overview-text">Brenwick Procurement Partners, LLC is a strategic management consulting firm headquartered in Oakmere, Maryland which provides a full suite of professional services and cutting edge solutions to government and private sector clientele in the Washington D.C. metropolitan area. We are process driven and results focused with the highest standard of ethics and integrity in all aspects of our business. Brenwick is a minority Economically Disadvantaged Woman-Owned Small Business (EDWOSB) that is dedicated to exceeding our clients’ expectations through lifecycle management that incorporates institutional knowledge and industry best practices to ensure that the highest possible quality in our end service delivery.</p>

  <svg class="why-band" viewBox="0 0 460 46" width="460" height="46">
    <rect x="0" y="8" width="460" height="38" fill="var(--gray-band)"/>
    <polygon points="225,8 340,-12 445,40" fill="var(--accent-blue)"/>
  </svg>
  <h2 class="section-head head-why">WHY CHOOSE US ?</h2>

  <div class="why-text">
    <p>Brenwick’s management and team of advisors have a proven track record of accomplishments with over 50+ years combined in industry leadership &amp; government service experience.</p>
    <p>Our extensive expertise in working alongside some of the industry’s top executives has gained us a unique competitive edge which enables us to develop customized solutions tailored to our customer’s specific needs...</p>
    <p>Brenwick welcomes the opportunity for strategic partnering and teaming alliances with small/mid-sized companies who bring added resources and past-experience to our project team.</p>
  </div>

  <div class="services-col"></div>

  <div class="service" style="top:270px;height:120px">
    <div class="service-label" style="top:18px">ACQUISITION<br>MANAGEMENT</div>
    <svg class="service-icon" style="top:58px" viewBox="0 0 96 50"><rect x="0" y="8" width="9" height="34" fill="var(--arrow-blue)"/><rect x="22" y="8" width="9" height="34" fill="var(--arrow-blue)"/><polygon points="46,2 94,25 46,48" fill="var(--arrow-blue)"/></svg>
    <p class="service-text" style="top:8px">Advisory, Acquisition Planning&amp; Strategy, Contract Cost Estimating &amp; Pricing, Contract Negotiation, Full Lifecycle contract administration, Procurement Package Development and Contract Closeout Support.</p>
  </div>

  <div class="service" style="top:390px;height:145px">
    <div class="service-label" style="top:22px">ADMINISTRATIVE<br>SUPPORT</div>
    <svg class="service-icon" style="top:62px" viewBox="0 0 96 50"><rect x="0" y="8" width="9" height="34" fill="var(--arrow-blue)"/><rect x="22" y="8" width="9" height="34" fill="var(--arrow-blue)"/><polygon points="46,2 94,25 46,48" fill="var(--arrow-blue)"/></svg>
    <p class="service-text" style="top:8px">Professional staffing support to government, public, private, and non-profit organizations providing outsourced confidential administrative and financial staff augmentation, bookkeeping, program &amp; project support, marketing and sales assistance as well as other related services.</p>
  </div>

  <div class="service" style="top:535px;height:116px">
    <div class="service-label" style="top:24px">BUSINESS<br>DEVELOPMENT</div>
    <svg class="service-icon" style="top:62px" viewBox="0 0 96 50"><rect x="0" y="8" width="9" height="34" fill="var(--arrow-blue)"/><rect x="22" y="8" width="9" height="34" fill="var(--arrow-blue)"/><polygon points="46,2 94,25 46,48" fill="var(--arrow-blue)"/></svg>
    <p class="service-text" style="top:6px">Business Branding, Capture Management, Documentation Compilation Support, Market Research &amp; Analysis, Proposal Development &amp; Coordination, Prospecting, Lead Generation and Small Business Commercialization.</p>
  </div>

  <div class="service" style="top:651px;height:135px">
    <div class="service-label" style="top:32px;left:-6px">LEGAL<br>SERVICES</div>
    <svg class="service-icon" style="top:74px" viewBox="0 0 96 50"><rect x="0" y="8" width="9" height="34" fill="var(--arrow-blue)"/><rect x="22" y="8" width="9" height="34" fill="var(--arrow-blue)"/><polygon points="46,2 94,25 46,48" fill="var(--arrow-blue)"/></svg>
    <p class="service-text" style="top:6px">Brenwick also provides legal counsel offerings providing a broad range of disciplines and projects. Offerings to include; Contract Business Law, Policy Advisory, FAR/DFAR Regulations, Collections Practice, Civil Litigation Support, Dispute Resolution, and Employment Law services.</p>
  </div>

  <div class="service" style="top:786px;height:122px">
    <div class="service-label" style="top:22px">PROCESS<br>IMPROVEMENT</div>
    <svg class="service-icon" style="top:62px" viewBox="0 0 96 50"><rect x="0" y="8" width="9" height="34" fill="var(--arrow-blue)"/><rect x="22" y="8" width="9" height="34" fill="var(--arrow-blue)"/><polygon points="46,2 94,25 46,48" fill="var(--arrow-blue)"/></svg>
    <p class="service-text" style="top:8px">Business Process Mapping &amp; Re-engineering, Change &amp; Transition Management, Quality Assurance, Risk Management &amp; Surveillance and Standard Operating Procedures, Strategic Policy &amp; Governance, Technical Writing Support.</p>
  </div>

  <div class="service" style="top:908px;height:206px;border-bottom:none">
    <div class="service-label" style="top:60px">PROCESS<br>IMPROVEMENT</div>
    <svg class="service-icon" style="top:104px" viewBox="0 0 96 50"><rect x="0" y="8" width="9" height="34" fill="var(--arrow-blue)"/><rect x="22" y="8" width="9" height="34" fill="var(--arrow-blue)"/><polygon points="46,2 94,25 46,48" fill="var(--arrow-blue)"/></svg>
    <p class="service-text" style="top:12px">Administrative Services, Federal Accounting Compliance &amp; Standards, Government Financial SystemTransactions &amp; Management Support, Factsheets, Technical &amp; Fiscal Business Cases, Performance Measurement, Government Infrastructure Functional Support and Independent Verification &amp; Validation (IV&amp;V), OMB Circulars and OMB Scorecard Results reporting.</p>
  </div>

  <footer class="footer">
    <div class="footer-title">Company Contact :</div>
    <div class="contact c-poc"><span class="label">Company POC :</span>Marisa T. Holloway</div>
    <div class="contact c-phone"><span class="label">Phone</span>: (202) 555-0147</div>
    <div class="contact c-email"><span class="label">Email</span>: info@brenwickpartners-example.com</div>
    <div class="contact c-addr"><span class="label">Address</span>: Oakmere, MD 20999</div>
  </footer>
</div>
</body>
</html>
```